Rack Card for Charter Sail Boat business in SF Bay

We are in need of a rack card design to highlight the business to tourists and locals. 2 sided card 3.86" x 8.39" (full bleed)

We are looking for visually appleaing designs on the front and back but a little more detail on the back.

Use the info provided (text and info) on the website to include the 3 key services (Quick, 1/2 day, fullday) and aspects of the boat, location and other key info for customers (not prices). DO NOT INCLUDE ALL THIS TEXT please pick the elements you would like to fit your design and inform the customer as you would like about the business.

I can also provide photos directly from the video if you think those would fit your design. If video doesn't work on this upload you can view it at the website or facebook page (www.fb.com/tidewinkcharters)

Now included a few video pictures in files for your use

Target Market(s)

Tourists and locals to san francisco east bay. 25 - 55 years old. Men and women.

Industry/Entity Type

Entertainment

Colors
0455a3
ec1f27
f3f1f8

Requirements
Must have
• Highlight services, key contact information (email, phone, website site), Visual impact
• 2-sided card - 3.86" x 8.39" (98 x 213 mm)
Nice to have
• facebook link, electric engine(green),

```html
<!DOCTYPE html>
<html lang="en">
<head>
<meta charset="utf-8">
<title>Tidewink Charters – Rack Card</title>
<link href="https://fonts.googleapis.com/css2?family=Kaushan+Script&family=Arimo:wght@400;700&family=Oswald:wght@500&display=swap" rel="stylesheet">
<style>
  :root{
    --blue:#0455a3;
    --blue-deep:#06327a;
    --red:#ec1f27;
    --red-deep:#b3121a;
    --paper:#f3f1f8;
    --white:#ffffff;
    --yellow:#ffe200;
    --ink:#1b1b1b;
    --stage:#d4d4d4;
  }
  *{box-sizing:border-box;margin:0;padding:0}
  html,body{width:1200px;height:1200px;overflow:hidden}
  body{background:radial-gradient(circle at 50% 45%,#efefef 0%,var(--stage) 100%);font-family:"Arimo",Arial,sans-serif;position:relative}
  .card{position:absolute;top:150px;width:414px;height:900px;background:var(--white);overflow:hidden;box-shadow:0 10px 30px rgba(0,0,0,.25)}
  .card--front{left:164px}
  .card--back{left:622px}
  .layer{position:absolute;left:0;top:0}

  .photo{position:absolute;border:6px solid var(--white);box-shadow:0 3px 8px rgba(0,0,0,.35)}
  .photo--hero{left:0;top:0;width:414px;height:350px;border:none;box-shadow:none;background:linear-gradient(180deg,#6f8fb0 0%,#e8c48c 40%,#3e5f86 62%,#1f3550 100%)}
  .photo--round{border-radius:50%}
  .photo--sail{left:218px;top:236px;width:156px;height:156px;background:radial-gradient(circle at 40% 30%,#e8eef4,#2f6fb6 70%)}
  .photo--cockpit{left:328px;top:360px;width:110px;height:110px;background:radial-gradient(circle at 50% 50%,#c9a36b,#4b3a2a 80%)}
  .photo--water{left:232px;top:396px;width:100px;height:100px;background:linear-gradient(180deg,#8fb8e6 0%,#2c66a8 55%,#12345c 100%)}
  .photo--marina{left:220px;top:480px;width:136px;height:136px;background:linear-gradient(180deg,#a9c7e8 0%,#5b7fa2 50%,#24425f 100%)}

  .brand{position:absolute;left:150px;top:28px;display:flex;align-items:center;gap:8px;white-space:nowrap;font-family:"Kaushan Script",cursive;font-size:26px;line-height:1;color:var(--blue)}
  .brand__dot{width:12px;height:12px;border-radius:50%;background:var(--red)}

  .tagline{position:absolute;left:20px;top:362px;width:200px;font-family:"Kaushan Script",cursive;font-size:20px;line-height:1.2;color:var(--white)}
  .tagline em{font-style:normal;color:var(--yellow)}

  .feature{position:absolute;color:var(--ink);font-size:12px;line-height:1.2}
  .feature h2{font-family:"Kaushan Script",cursive;font-weight:400;font-size:30px;line-height:1;margin-bottom:4px}
  .feature--modern{left:22px;top:552px;width:190px}
  .feature--modern h2,.feature--safe h2{color:var(--red)}
  .feature--entertain{left:22px;top:682px;width:200px}
  .feature--entertain h2{color:var(--blue)}
  .feature--safe{left:234px;top:628px;width:168px;font-size:11.5px}

  .contact-strip{position:absolute;left:22px;bottom:12px;color:var(--white);font-family:"Oswald",sans-serif;font-size:15px;line-height:1.45}
  .contact-strip li,.contact-grid li{list-style:none;display:flex;align-items:center;gap:8px;white-space:nowrap}
  .icon{width:18px;height:18px;flex:none}

  .trip{position:absolute;left:22px;top:18px;width:372px;color:var(--white)}
  .trip h2{font-family:"Kaushan Script",cursive;font-weight:400;font-size:30px;line-height:1;margin-bottom:6px}
  .trip p{font-size:10.5px;line-height:1.25}
  .map{position:absolute;left:0;top:150px;width:414px;height:640px;background:linear-gradient(160deg,#dbe9f5 0%,#c6dcf0 45%,#e6eef2 100%)}
  .service{position:absolute;border-radius:50%;border:5px solid var(--white);box-shadow:0 4px 10px rgba(0,0,0,.35);color:var(--white);text-align:center;display:flex;flex-direction:column;justify-content:center;align-items:center;padding:0 20px;font-size:10.5px;line-height:1.25}
  .service h3{font-family:"Kaushan Script",cursive;font-weight:400;font-size:20px;line-height:1.05;color:var(--yellow);margin-bottom:4px}
  .service--blast{left:240px;top:150px;width:160px;height:160px;background:radial-gradient(circle at 40% 35%,#f4474d,var(--red-deep))}
  .service--half{left:40px;top:315px;width:176px;height:176px;background:radial-gradient(circle at 40% 35%,#2a78c9,var(--blue-deep))}
  .service--full{left:230px;top:505px;width:166px;height:166px;background:radial-gradient(circle at 40% 35%,#34a853,#0f5a24)}
  .badge{position:absolute;left:14px;top:778px;width:54px;height:54px;border-radius:50%;background:var(--paper);border:3px solid #d7b43a}
  .contact-title{position:absolute;left:124px;top:766px;font-family:"Kaushan Script",cursive;font-size:36px;color:var(--white)}
  .contact-grid{position:absolute;left:22px;top:836px;width:380px;display:grid;grid-template-columns:1fr 1.35fr;gap:6px 10px;color:var(--white);font-family:"Oswald",sans-serif;font-size:13px}
</style>
</head>
<body>

<section class="card card--front" aria-label="Rack card front">
  <div class="photo photo--hero" role="img" aria-label="Photo from the deck of a sailboat at sunset on San Francisco Bay"></div>

  <svg class="layer" width="414" height="900" viewBox="0 0 414 900" aria-hidden="true">
    <path d="M0 330 C120 300 260 310 414 280 L414 296 C260 326 120 316 0 346 Z" fill="var(--red)"/>
    <path d="M0 342 C120 312 260 322 414 292 L414 520 C300 530 170 490 0 540 Z" fill="var(--blue)"/>
    <path d="M250 570 C320 600 370 590 414 572 L414 584 C370 604 320 612 250 570 Z" fill="var(--red)"/>
    <path d="M0 830 C140 826 280 820 414 812 L414 826 C280 834 140 840 0 844 Z" fill="var(--red)"/>
    <path d="M0 840 C140 836 280 830 414 822 L414 900 L0 900 Z" fill="var(--blue)"/>
  </svg>

  <div class="brand"><span class="brand__dot"></span>Tidewink Charters</div>

  <p class="tagline">Enjoy an amazing experience aboard <em>Tidewink</em> and view San Francisco and the rest of the bay</p>

  <div class="photo photo--round photo--sail" role="img" aria-label="Photo of the mainsail against blue sky"></div>
  <div class="photo photo--round photo--cockpit" role="img" aria-label="Photo of the cockpit cushions"></div>
  <div class="photo photo--round photo--water" role="img" aria-label="Photo of sunlight on the bay water"></div>
  <div class="photo photo--round photo--marina" role="img" aria-label="Photo of the boat moored at the marina"></div>

  <div class="feature feature--modern">
    <h2>Modern</h2>
    <p>Tidewink is completely electric which means no diesel smells, noise or vibration to suffer. New electrics, plumbing, toilets, and deck areas compliment the elegant lines.</p>
  </div>
  <div class="feature feature--entertain">
    <h2>Entertaining</h2>
    <p>Experience the thrill of sailing Tidewink while we explore Alcatraz and Angel Islands', The Golden Gate and Bay Bridges, the City front or the many other hidden gems.</p>
  </div>
  <div class="feature feature--safe">
    <h2>Safe</h2>
    <p>We carry aboard everything to make your time aboard safe. Life preservers and USCG bulky ones as well as modern self inflating slim comfortable life jackets. Also loaded for every trip is a complete first aid kit, AED, EPIRB, and many other safety items.</p>
  </div>

  <ul class="contact-strip">
    <li><svg class="icon" viewBox="0 0 24 24"><circle cx="12" cy="12" r="11" fill="none" stroke="var(--white)" stroke-width="1.6"/><path d="M8 6.5l2 .2 1 2.8-1.4 1a7 7 0 003.9 3.9l1-1.4 2.8 1 .2 2a1.5 1.5 0 01-1.6 1.4A10 10 0 016.6 8.1 1.5 1.5 0 018 6.5z" fill="var(--white)"/></svg>+1 (510) 555 SAIL (7245)</li>
    <li><svg class="icon" viewBox="0 0 24 24"><rect x="2" y="5" width="20" height="14" fill="none" stroke="var(--white)" stroke-width="1.6"/><path d="M2 5l10 8 10-8" fill="none" stroke="var(--white)" stroke-width="1.6"/></svg>Bookings@TidewinkCharters.com</li>
  </ul>
</section>

<section class="card card--back" aria-label="Rack card back">
  <div class="map" role="img" aria-label="Map of San Francisco Bay with three dotted sailing routes"></div>

  <svg class="layer" width="414" height="900" viewBox="0 0 414 900" aria-hidden="true">
    <path d="M0 0 H414 V128 C300 150 160 150 0 190 Z" fill="var(--blue)"/>
    <path d="M0 190 C160 150 300 150 414 128 L414 140 C300 164 160 166 0 204 Z" fill="var(--red)"/>
    <path d="M0 204 C160 166 300 164 414 140 L414 146 C300 170 160 172 0 210 Z" fill="var(--white)"/>
    <path d="M110 300 L300 235 M120 410 L414 370 M80 520 L414 540" stroke="var(--blue)" stroke-width="2" fill="none" opacity=".7"/>
    <path d="M0 780 C140 780 300 740 414 690 L414 706 C300 756 140 796 0 796 Z" fill="var(--red)"/>
    <path d="M0 792 C140 792 300 752 414 702 L414 900 L0 900 Z" fill="var(--blue)"/>
  </svg>

  <div class="trip">
    <h2>The trip</h2>
    <p>When chartering Tidewink, the vessel is yours to direct anywhere within the time you wish to enjoy her. We do have a few old favorites that are always fun that we have listed below. These are just to provide an idea of the possible cruise as every trip takes into account your ideas and natures (tides, weather and currents) will. Our custom trips are simple to arrange and book, we simply ask for a minimum of 3 hours duration.</p>
  </div>

  <div class="service service--blast">
    <h3>2 hours Blast</h3>
    <p>Could be a sunset sail, an early morning wake up cruise or a blast out into the bay anytime to find peace, fresh air and amazing views.</p>
  </div>
  <div class="service service--half">
    <h3>½ day Fun</h3>
    <p>A full morning, afternoon or evening out in the Bay seeing many of the main features and landmarks close to the Bay from the water. Actual duration 4-5 hours</p>
  </div>
  <div class="service service--full">
    <h3>Full Day Adventure</h3>
    <p>The day includes a complete circuit of the Bay and lunch at anchor. Actual duration 7-8 hours</p>
  </div>

  <div class="badge" role="img" aria-label="Licensed captain badge"></div>
  <div class="contact-title">Contact</div>

  <ul class="contact-grid">
    <li><svg class="icon" viewBox="0 0 24 24"><circle cx="12" cy="12" r="11" fill="none" stroke="var(--white)" stroke-width="1.6"/><path d="M8 6.5l2 .2 1 2.8-1.4 1a7 7 0 003.9 3.9l1-1.4 2.8 1 .2 2a1.5 1.5 0 01-1.6 1.4A10 10 0 016.6 8.1 1.5 1.5 0 018 6.5z" fill="var(--white)"/></svg>+1 (510) 555 SAIL (7245)</li>
    <li><svg class="icon" viewBox="0 0 24 24"><rect x="2" y="5" width="20" height="14" fill="none" stroke="var(--white)" stroke-width="1.6"/><path d="M2 5l10 8 10-8" fill="none" stroke="var(--white)" stroke-width="1.6"/></svg>Bookings@TidewinkCharters.com</li>
    <li><svg class="icon" viewBox="0 0 24 24"><circle cx="12" cy="12" r="10" fill="none" stroke="var(--white)" stroke-width="1.6"/><ellipse cx="12" cy="12" rx="4.5" ry="10" fill="none" stroke="var(--white)" stroke-width="1.4"/><path d="M2 12h20" stroke="var(--white)" stroke-width="1.4"/></svg>www.tidewinkcharters.com</li>
    <li><svg class="icon" viewBox="0 0 24 24"><circle cx="12" cy="12" r="10" fill="none" stroke="var(--white)" stroke-width="1.6"/></svg>/tidewinkcharters</li>
  </ul>
</section>

</body>
</html>
```